Stationery Design Project

Hi All,

We need you to design stationary for a new Business and Accounting Advisory Firm. We have already got the logo designed and it is attached. If you could also if possible, match the fonts in your design to that on the logo’s provided.

What we need:
- Business Card
- A4 Letter head
- A4 Folders
- PPT template (Title page and regular page)

And what ever else you want to throw in.

We are in the process of getting the web site designed, however below is a list of websites which we like which will give you an understanding of the style that we are going for.

- plavoni.com
- brightfunnelo.com
- hourquillet.com
- artmarrowly.com

I look forward to your seeing your design.

Hi All,

I have just realised that I forgot that i need to include a Licensed Tallymasters image on the letter head, please find attaced as File 1. Could you please have this image in the bottom left header.

Regards,

Gareth

Industry/Entity Type

Business

Requirements
Must have
• Outputs:
- Documents ready to print
- Generic editable information
- Pdf copies of the documents
- Word version of letterhead

```html
<!DOCTYPE html>
<html lang="en">
<head>
<meta charset="utf-8">
<title>Ardenvale Partners – Business Cards</title>
<link href="https://fonts.googleapis.com/css2?family=PT+Sans:ital,wght@0,400;0,700;1,700&display=swap" rel="stylesheet">
<style>
  :root {
    --page-bg: #ecebe8;
    --blue-deep: #2c4f9c;
    --blue-mid: #3a78bd;
    --blue-light: #42b8d9;
    --orange: #f08a24;
    --orange-light: #fbb13c;
    --white: #ffffff;
    --ink-blue: #2a4a94;
  }
  * { margin: 0; padding: 0; box-sizing: border-box; }
  html, body { width: 1200px; height: 900px; overflow: hidden; }
  body {
    background: var(--page-bg);
    font-family: "PT Sans", Arial, sans-serif;
    position: relative;
  }
  .card {
    position: absolute;
    left: 300px;
    width: 600px;
    height: 343px;
    overflow: hidden;
    box-shadow: 0 6px 18px rgba(0,0,0,0.18);
  }
  .card-front {
    top: 70px;
    background: linear-gradient(115deg, var(--blue-deep) 0%, var(--blue-mid) 55%, var(--blue-light) 100%);
    display: flex;
    align-items: center;
    justify-content: center;
  }
  .brand-name {
    display: flex;
    align-items: center;
    gap: 12px;
    font-weight: 700;
    font-size: 34px;
    letter-spacing: 0.5px;
    white-space: nowrap;
  }
  .card-front .brand-name { color: var(--white); }
  .brand-dot {
    flex: none;
    width: 16px; height: 16px; border-radius: 50%;
    background: var(--white);
  }
  .card-back { top: 487px; background: var(--white); }
  .card-back svg.back-shapes { position: absolute; inset: 0; }
  .card-back .brand-name {
    position: absolute;
    left: 28px; top: 96px;
    gap: 9px;
    color: var(--ink-blue);
    font-size: 22px;
    letter-spacing: 0.2px;
  }
  .card-back .brand-dot { background: var(--orange); width: 12px; height: 12px; }
  .holder {
    position: absolute;
    left: 380px; top: 38px;
    color: var(--white);
  }
  .holder-name { font-weight: 700; font-size: 17px; }
  .holder-role { font-size: 13px; }
  .contact-list {
    position: absolute;
    left: 330px; top: 116px;
    list-style: none;
    color: var(--white);
    font-size: 14.5px;
    line-height: 21px;
  }
  .contact-list li { display: flex; align-items: flex-start; gap: 10px; }
  .contact-icon { flex: none; width: 16px; height: 16px; margin-top: 2px; }
</style>
</head>
<body>

<section class="card card-front" aria-label="Business card front">
  <div class="brand-name"><span class="brand-dot"></span>Ardenvale Partners</div>
</section>

<section class="card card-back" aria-label="Business card back">
  <svg class="back-shapes" width="600" height="343" viewBox="0 0 600 343">
    <defs>
      <linearGradient id="panelBlue" x1="0" y1="1" x2="1" y2="0">
        <stop offset="0" stop-color="#2c4f9c"/>
        <stop offset="0.6" stop-color="#3a78bd"/>
        <stop offset="1" stop-color="#42a6d6"/>
      </linearGradient>
      <linearGradient id="swoosh" x1="0" y1="1" x2="1" y2="0">
        <stop offset="0" stop-color="#fbb13c"/>
        <stop offset="1" stop-color="#f08a24"/>
      </linearGradient>
    </defs>
    <path d="M395 0 C300 45 240 180 258 343 L250 343 C226 180 290 40 380 0 Z" fill="url(#swoosh)"/>
    <path d="M232 343 C214 250 236 170 290 110 C248 175 236 250 246 343 Z" fill="url(#swoosh)"/>
    <path d="M420 0 C318 50 262 190 276 343 L600 343 L600 0 Z" fill="url(#panelBlue)"/>
  </svg>

  <div class="brand-name"><span class="brand-dot"></span>Ardenvale Partners</div>

  <div class="holder">
    <div class="holder-name">Tobias Renwick</div>
    <div class="holder-role">Director</div>
  </div>

  <ul class="contact-list">
    <li>
      <svg class="contact-icon" viewBox="0 0 16 16"><circle cx="8" cy="8" r="8" fill="#f5a12e"/><path d="M8 3.5a3 3 0 0 0-3 3c0 2.2 3 5.5 3 5.5s3-3.3 3-5.5a3 3 0 0 0-3-3zm0 4.2a1.2 1.2 0 1 1 0-2.4 1.2 1.2 0 0 1 0 2.4z" fill="#fff"/></svg>
      <span>Brinkstraat 27-C4<br>5678 KL, Harlingen</span>
    </li>
    <li>
      <svg class="contact-icon" viewBox="0 0 16 16"><circle cx="8" cy="8" r="8" fill="#f5a12e"/><path d="M5.2 4h1.6l.7 2-1 .7a5 5 0 0 0 2.6 2.6l.7-1 2 .7v1.6c0 .5-.4.9-.9.9A7 7 0 0 1 4.3 4.9c0-.5.4-.9.9-.9z" fill="#fff"/></svg>
      <span>555-014-2930</span>
    </li>
    <li>
      <svg class="contact-icon" viewBox="0 0 16 16"><circle cx="8" cy="8" r="8" fill="#f5a12e"/><rect x="4.5" y="4" width="7" height="3" fill="#fff"/><rect x="3.5" y="7.5" width="9" height="4.5" rx="1" fill="#fff"/></svg>
      <span>555-014-2939</span>
    </li>
    <li>
      <svg class="contact-icon" viewBox="0 0 16 16"><circle cx="8" cy="8" r="8" fill="#f5a12e"/><circle cx="8" cy="8" r="1.8" fill="none" stroke="#fff" stroke-width="1.3"/><path d="M9.8 6.4v2.4c0 1 1.6 1 1.6-.4A3.4 3.4 0 1 0 10 11" fill="none" stroke="#fff" stroke-width="1.3"/></svg>
      <span>tobias@ardenvalepartners.com</span>
    </li>
    <li>
      <svg class="contact-icon" viewBox="0 0 16 16"><circle cx="8" cy="8" r="8" fill="#f5a12e"/><circle cx="8" cy="8" r="4" fill="none" stroke="#fff" stroke-width="1.1"/><ellipse cx="8" cy="8" rx="1.6" ry="4" fill="none" stroke="#fff" stroke-width="1"/><path d="M4 8h8" stroke="#fff" stroke-width="1"/></svg>
      <span>www.ardenvalepartners.com</span>
    </li>
  </ul>
</section>

</body>
</html>
```